Brightway Gate works Business cards/Stationery
Business cards and stationery
Brightway Gate works Business cards/Stationery -
Creative Brief
Use specific fonts
Whatever you think looks best
Professional
Paul Hendley
Owner
248 Marlow Ridge Rd. Easley, SC 29642
Brightwaygateworks@mailnest.net
www.Brightwaygateworks.net
Use tagline: A Brighter Way Through Every Gate
I would like to see something unique with the logo on the back.

```html
<!DOCTYPE html>
<html lang="en">
<head>
<meta charset="utf-8">
<title>Brightway Gate works – Business Card</title>
<link rel="stylesheet" href="https://fonts.googleapis.com/css2?family=Source+Sans+3:ital,wght@0,400;0,600;0,700;1,600&display=swap">
<style>
  :root {
    --bg: #e9e6e1;
    --card: #ffffff;
    --brand-red: #8e1b1b;
    --band-dark: #3a0c0c;
    --band-mid: #6e1818;
    --ink: #2b2b2b;
    --rule: #9a9a9a;
  }
  * { box-sizing: border-box; margin: 0; padding: 0; }
  html, body { width: 1200px; height: 965px; overflow: hidden; }
  body {
    background: var(--bg);
    font-family: "Source Sans 3", Arial, sans-serif;
    color: var(--ink);
    position: relative;
  }
  .card {
    position: absolute;
    left: 243px; top: 235px;
    width: 770px; height: 450px;
    background: var(--card);
    border-radius: 24px;
    overflow: hidden;
    box-shadow: 0 4px 14px rgba(0,0,0,0.18);
  }
  .card__band {
    position: absolute; left: 0; top: 0; bottom: 0;
    width: 36px;
    background: linear-gradient(90deg, var(--band-dark), var(--band-mid) 55%, var(--band-dark));
  }
  .card__band-rule {
    position: absolute; left: 43px; top: 0; bottom: 0;
    width: 3px; background: var(--band-dark);
  }
  .brand {
    position: absolute; left: 109px; top: 60px;
    display: flex; align-items: center; gap: 16px;
    white-space: nowrap;
  }
  .brand__mark {
    width: 46px; height: 46px; background: var(--brand-red);
  }
  .brand__name {
    font-size: 48px; font-weight: 700; color: var(--brand-red);
    letter-spacing: 0.5px; line-height: 1;
  }
  .owner {
    position: absolute; right: 492px; top: 218px;
    text-align: right; white-space: nowrap;
  }
  .owner__name { font-size: 31px; font-weight: 700; color: var(--brand-red); line-height: 1.1; }
  .owner__title { font-size: 20px; font-weight: 600; font-style: italic; color: var(--ink); margin-top: 4px; }
  .owner__address { font-size: 21px; color: var(--ink); margin-top: 14px; line-height: 1.3; }
  .divider {
    position: absolute; left: 305px; top: 220px;
    width: 2px; height: 138px; background: var(--rule);
  }
  .contacts {
    position: absolute; left: 340px; top: 222px;
    list-style: none; white-space: nowrap;
  }
  .contacts__item {
    display: flex; align-items: center; gap: 14px;
    height: 34px; font-size: 21px; color: var(--ink);
  }
  .contacts__icon { width: 20px; height: 20px; fill: var(--brand-red); flex: none; }
  .tagline {
    position: absolute; left: 46px; right: 0; top: 390px;
    text-align: center; white-space: nowrap;
    font-size: 24px; font-weight: 600; font-style: italic;
    color: var(--brand-red); letter-spacing: 0.6px;
  }
</style>
</head>
<body>
  <main class="card">
    <div class="card__band"></div>
    <div class="card__band-rule"></div>

    <header class="brand">
      <span class="brand__mark"></span>
      <span class="brand__name">Brightway Gate works</span>
    </header>

    <section class="owner">
      <p class="owner__name">Paul Hendley</p>
      <p class="owner__title">Owner</p>
      <p class="owner__address">248 Marlow Ridge Rd.<br>Easley, SC 29642</p>
    </section>

    <div class="divider"></div>

    <ul class="contacts">
      <li class="contacts__item">
        <svg class="contacts__icon" viewBox="0 0 24 24"><path d="M6.6 10.8c1.4 2.8 3.8 5.1 6.6 6.6l2.2-2.2c.3-.3.7-.4 1-.2 1.1.4 2.3.6 3.6.6.6 0 1 .4 1 1V20c0 .6-.4 1-1 1C10.6 21 3 13.4 3 4c0-.6.4-1 1-1h3.5c.6 0 1 .4 1 1 0 1.3.2 2.5.6 3.6.1.3 0 .7-.2 1L6.6 10.8z"/></svg>
        <span>(864)-555-0148</span>
      </li>
      <li class="contacts__item">
        <svg class="contacts__icon" viewBox="0 0 24 24"><path d="M7 2h10v5H7z"/><path d="M4 8h16a2 2 0 0 1 2 2v7h-4v5H6v-5H2v-7a2 2 0 0 1 2-2zm4 8v4h8v-4z"/></svg>
        <span>(864)-555-0192</span>
      </li>
      <li class="contacts__item">
        <svg class="contacts__icon" viewBox="0 0 24 24"><path d="M12 2a10 10 0 1 0 5 18.7l-1-1.7A8 8 0 1 1 20 12v1.5a1.5 1.5 0 0 1-3 0V7h-2v1a5 5 0 1 0 .6 7.3A3.5 3.5 0 0 0 22 13.5V12A10 10 0 0 0 12 2zm0 13a3 3 0 1 1 0-6 3 3 0 0 1 0 6z"/></svg>
        <span>Brightwaygateworks@mailnest.net</span>
      </li>
      <li class="contacts__item">
        <svg class="contacts__icon" viewBox="0 0 24 24"><path d="M12 2a10 10 0 1 0 0 20 10 10 0 0 0 0-20zm6.9 9h-3a15 15 0 0 0-1.4-6.1A8 8 0 0 1 18.9 11zM12 4.1c.9 1.2 1.8 3.6 1.9 6.9h-3.8c.1-3.3 1-5.7 1.9-6.9zM9.5 4.9A15 15 0 0 0 8.1 11h-3a8 8 0 0 1 4.4-6.1zM5.1 13h3a15 15 0 0 0 1.4 6.1A8 8 0 0 1 5.1 13zm6.9 6.9c-.9-1.2-1.8-3.6-1.9-6.9h3.8c-.1 3.3-1 5.7-1.9 6.9zm2.5-.8a15 15 0 0 0 1.4-6.1h3a8 8 0 0 1-4.4 6.1z"/></svg>
        <span>www.Brightwaygateworks.net</span>
      </li>
    </ul>

    <p class="tagline">A Brighter Way Through Every Gate</p>
  </main>
</body>
</html>
```